Corporate Design für Portweinhandel
Zielgruppe
Portweinhandel, Tastings
Aufgabenstellung
Es soll entweder eine Portweinflasche mit LP drinnen, oder eine Traubenrebe mit LP drinnen, oder LP als Logo sein. Darunter soll Lindahl Portwein gerade oder im Halbkreis unter dem Logo stehen.

```html
<!DOCTYPE html>
<html lang="de">
<head>
<meta charset="utf-8">
<title>Lindahl Portwein – Corporate Design</title>
<link href="https://fonts.googleapis.com/css2?family=Montserrat:wght@700&family=Cormorant+Garamond:ital,wght@1,500&display=swap" rel="stylesheet">
<style>
  :root{
    --wine:#a3121f;
    --ink:#1d1d1f;
    --paper:#ffffff;
    --bg:#f3f3f3;
    --shadow:0 3px 8px rgba(0,0,0,.22);
  }
  *{box-sizing:border-box;margin:0;padding:0}
  html,body{width:1200px;height:523px;overflow:hidden;background:var(--bg)}
  .canvas{position:relative;width:1200px;height:523px}
  .sans{font-family:"Montserrat",sans-serif;font-weight:700;letter-spacing:.02em}
  .serif{font-family:"Cormorant Garamond",serif;font-style:italic;font-weight:500}

  /* Wordmark */
  .wordmark{position:absolute;display:flex;flex-direction:column;align-items:flex-start}
  .wordmark .name{color:var(--ink);text-transform:uppercase;white-space:nowrap}
  .wordmark .tagline{color:var(--wine);text-transform:uppercase;letter-spacing:.12em;white-space:nowrap}
  .wordmark .dot{display:inline-block;border-radius:50%;background:var(--wine);vertical-align:middle}

  .logo-main{left:80px;top:205px}
  .logo-main .name{font-size:38px}
  .logo-main .tagline{font-size:17px;margin-top:4px}
  .logo-main .dot{width:30px;height:30px;margin-right:14px}

  /* Business cards */
  .card{position:absolute;width:232px;height:150px;background:var(--paper);box-shadow:var(--shadow)}
  .card-front{left:560px;top:70px;display:flex;align-items:center;justify-content:center}
  .card-front .wordmark{position:static}
  .card-front .name{font-size:14px}
  .card-front .tagline{font-size:7px;margin-top:2px}
  .card-back{left:560px;top:290px;padding:22px 14px}
  .card-back .title{color:var(--wine);font-size:11px}
  .card-back .details{margin-top:8px;font-size:9.5px;line-height:1.3;color:var(--ink)}

  /* Letterhead */
  .letter{position:absolute;left:830px;top:14px;width:345px;height:488px;background:var(--paper);box-shadow:var(--shadow)}
  .letter .logo-small{right:20px;top:52px;align-items:flex-end}
  .letter .logo-small .name{font-size:7px}
  .letter .logo-small .tagline{font-size:4px;margin-top:1px}
  .sender-line{position:absolute;left:40px;top:89px;font-size:3.4px;color:var(--ink);white-space:nowrap}
  .sender-line b{color:var(--wine)}
  .address{position:absolute;right:20px;top:88px;text-align:right;font-size:4.2px;line-height:1.75;color:var(--ink)}
  .address .title{color:var(--wine);font-size:4.4px}
  .fold{position:absolute;left:0;width:5px;height:1px;background:var(--wine)}
  .footer-rule{position:absolute;left:0;right:0;top:438px;height:1px;background:var(--wine)}
  .footer{position:absolute;top:452px;font-size:4.2px;line-height:1.7;color:var(--ink)}
  .footer .title{color:var(--wine);font-size:4.4px}
</style>
</head>
<body>
<main class="canvas">

  <section class="wordmark logo-main">
    <span class="name sans"><span class="dot"></span>Lindahl Portwein</span>
    <span class="tagline serif">Portweinhandel &amp; Tastings</span>
  </section>

  <article class="card card-front">
    <div class="wordmark">
      <span class="name sans">Lindahl Portwein</span>
      <span class="tagline serif">Portweinhandel &amp; Tastings</span>
    </div>
  </article>

  <article class="card card-back">
    <h2 class="title sans">LINDAHL PORTWEIN</h2>
    <p class="details serif">
      Musterstraße 123<br>
      12345 Musterstadt<br>
      Tel.: 0123 45678<br>
      Fax: 0123 456788<br>
      info@lindahlportwein@mail.de<br>
      www.lindahlportwein.de
    </p>
  </article>

  <article class="letter">
    <div class="wordmark logo-small">
      <span class="name sans">Lindahl Portwein</span>
      <span class="tagline serif">Portweinhandel &amp; Tastings</span>
    </div>

    <p class="sender-line serif"><b class="sans">LINDAHL PORTWEIN</b> • Musterstraße 123 • 12345 Musterstadt</p>

    <address class="address serif">
      <span class="title sans">LINDAHL PORTWEIN</span><br>
      Musterstraße 123<br>
      12345 Musterstadt<br>
      Tel.: 0123 45678<br>
      Fax: 0123 456788<br>
      info@lindahlportwein.de<br>
      www.lindahlportwein.de
    </address>

    <span class="fold" style="top:173px"></span>
    <span class="fold" style="top:245px"></span>
    <span class="fold" style="top:345px"></span>

    <div class="footer-rule"></div>
    <div class="footer serif" style="left:33px">
      <span class="title sans">LINDAHL PORTWEIN</span><br>
      Musterstraße 123<br>
      12345 Musterstadt
    </div>
    <div class="footer serif" style="left:125px">
      USt-IDNR: CHE-481.226.309<br>
      MWST
    </div>
    <div class="footer serif" style="left:245px">
      Alpen Kreditbank<br>
      IBAN: DE 12 3456 7890 1234 5678 0<br>
      Clearing: 1234<br>
      SWIFT/BIC: ALPKCHZZ80
    </div>
  </article>

</main>
</body>
</html>
```